Brantor Energy Services Website - Solar Sales and Installation and Renewable Energy Marketing

I need a website for my solar sales and installation/renewable energy marketing company. We will focus on solar, so the web page should make that a main focus. Ideally it will have 5-6 total pages. One main page, one page "Why Solar", "Our Services", "About Us", "Contact Us", and some type of page that collects leads or information from customers who are interested in a solar quote. Our image focus should be either residential solar panels or windmills (renewable energy). The logo, attached, is green and orange. The color scheme should be predominantly white, clean cut, with orange/green buttons or accents. I don't want to have a blog-like page, it should mimic other solar company websites. A good example would be Calderby's solar website.

```html
<!DOCTYPE html>
<html lang="en">
<head>
<meta charset="utf-8">
<title>Brantor Energy Services</title>
<link href="https://fonts.googleapis.com/css2?family=Montserrat:wght@400;500;600;700;800&family=Open+Sans:wght@400;600&display=swap" rel="stylesheet">
<style>
:root{
  --orange:#f7741a;
  --green:#8ed424;
  --lime:#a6e22e;
  --dark:#333;
  --text:#555;
  --muted:#888;
  --white:#fff;
  --sky-top:#1a5fd1;
  --sky-mid:#59a7ec;
  --grass:#5da32a;
  --social:#1f5fa8;
  --line:#e6e6e6;
}
*{box-sizing:border-box;margin:0;padding:0}
html,body{width:1200px;height:3352px;overflow:hidden;background:var(--white)}
body{font-family:"Open Sans",Arial,sans-serif;color:var(--text);position:relative}
h1,h2,h3,h4,.nav,.btn{font-family:"Montserrat",Arial,sans-serif}

/* hero */
.hero{position:absolute;top:0;left:0;width:1200px;height:680px;
  background:linear-gradient(180deg,var(--sky-top) 0%,var(--sky-mid) 45%,#b9d6ee 66%,#9c8a74 70%,#c9b79c 84%,var(--grass) 92%,#3f8a1e 100%)}
.header{position:absolute;top:0;left:0;right:0;height:78px;display:flex;align-items:center;padding:0 36px}
.brand{display:flex;align-items:center;gap:12px;font-family:"Montserrat",sans-serif;font-weight:700;color:var(--white);font-size:15px;line-height:1.1;width:190px}
.brand .dot{width:40px;height:40px;border-radius:50%;background:var(--green);flex:none}
.nav{margin-left:auto;display:flex;gap:34px;font-size:16px;color:var(--white);align-items:center}
.nav .active{color:var(--orange)}
.hero-title{position:absolute;top:138px;width:100%;text-align:center;color:var(--white)}
.hero-title h3{font-weight:500;font-size:30px;letter-spacing:1px}
.hero-title h1{font-weight:800;font-size:72px;letter-spacing:1px;margin-top:2px}

/* call bar */
.callbar{position:absolute;top:680px;left:0;width:1200px;height:80px;background:var(--lime);display:flex;align-items:center;justify-content:space-between;padding:0 28px 0 84px}
.callbar p{font-family:"Montserrat",sans-serif;font-weight:700;color:var(--white);font-size:22px}
.phone-pill{background:var(--orange);color:var(--white);border-radius:30px;height:56px;padding:0 30px 0 18px;display:flex;align-items:center;gap:18px;font-family:"Montserrat",sans-serif;font-weight:700;font-size:22px}
.phone-pill .ic{width:38px;height:38px;border-radius:50%;background:var(--white);display:flex;align-items:center;justify-content:center}

/* about */
.about{position:absolute;top:760px;left:0;width:1200px;height:528px;text-align:center}
.about h3{margin-top:80px;font-size:30px;font-weight:600;color:var(--dark)}
.about h2{font-size:44px;font-weight:600;color:var(--dark);margin-top:2px}
.about .rule{width:70px;height:4px;background:var(--green);margin:16px auto 30px}
.about p{width:460px;margin:0 auto 24px;font-size:15px;line-height:1.8;color:var(--muted)}
.round-btn{width:46px;height:46px;border-radius:50%;background:var(--orange);margin:14px auto 0;display:flex;align-items:center;justify-content:center}

/* why solar */
.why{position:absolute;top:1288px;left:0;width:1200px;height:632px;
  background:linear-gradient(180deg,#2b6fd0 0%,#6fb0ec 45%,#e8e2dc 60%,#c86a3a 70%,#f0eee9 82%,#5aa02d 92%,#3c8220 100%)}
.why-panel{position:absolute;top:152px;left:0;width:580px;height:380px;background:rgba(255,255,255,.92);padding:44px 0 0 84px}
.why-panel h2{font-size:46px;font-weight:700;color:var(--dark)}
.why-panel .lead{width:340px;font-size:15px;line-height:1.6;color:var(--dark);margin-top:6px}
.features{display:grid;grid-template-columns:250px 220px;row-gap:36px;margin-top:34px}
.feature{display:flex;align-items:center;gap:14px;font-family:"Montserrat",sans-serif;font-weight:700;font-size:17px;color:var(--dark)}
.feature .sq{width:60px;height:60px;background:var(--orange);border-radius:6px;display:flex;align-items:center;justify-content:center;flex:none}

/* services */
.services{position:absolute;top:1920px;left:0;width:1200px;height:560px;text-align:center}
.services h2{margin-top:80px;font-size:46px;font-weight:600;color:var(--dark)}
.services .sub{font-size:15px;color:var(--dark);margin-top:4px}
.svc-row{display:flex;justify-content:center;gap:56px;margin-top:36px}
.svc{width:140px}
.svc .ph{width:140px;height:136px}
.svc h4{font-size:20px;font-weight:500;color:var(--dark);margin-top:20px}
.svc p{font-size:14px;line-height:1.5;color:var(--muted);margin-top:6px}
.btn{display:inline-block;background:var(--orange);color:var(--white);font-weight:600;font-size:18px;padding:14px 28px;border-radius:30px;margin-top:24px}

/* contact */
.contact{position:absolute;top:2480px;left:0;width:1200px;height:600px;
  background:linear-gradient(180deg,#1d6ad4 0%,#79b6ec 40%,#d6e6f3 62%,#7bb840 80%,#4f9a22 100%)}
.contact .house{position:absolute;left:0;top:150px;width:640px;height:380px;background:linear-gradient(180deg,#6b5a4b 0%,#b89e82 40%,#d9c6ab 75%,#7a9a52 100%)}
.contact-form{position:absolute;left:684px;top:50px;width:420px}
.contact-form h2{font-size:44px;font-weight:500;color:var(--dark)}
.contact-form .note{font-size:14px;color:var(--dark);margin-top:12px}
.contact-form .tel{font-size:16px;font-weight:700;color:var(--orange);margin-top:2px;font-family:"Montserrat",sans-serif}
.field{background:var(--white);height:44px;margin-top:14px;padding:10px 14px;font-size:14px;color:var(--muted);border:1px solid var(--line)}
.field:first-of-type{border-color:var(--orange)}
.field.msg{height:96px}
.field .req{color:var(--orange)}

/* footer */
.footer{position:absolute;top:3080px;left:0;width:1200px;height:272px;border-top:6px solid var(--lime);display:flex;padding:40px 0 0 100px}
.f-brand{width:240px}
.f-brand .name{display:flex;align-items:center;gap:12px;font-family:"Montserrat",sans-serif;font-weight:700;font-size:20px;color:var(--dark);line-height:1.15}
.f-brand .dot{width:56px;height:56px;border-radius:50%;background:var(--green);flex:none}
.f-brand p{font-size:12px;color:var(--muted);margin-top:18px;line-height:1.5}
.f-col{width:220px;margin-left:60px}
.f-col h4{font-size:20px;font-weight:600;color:var(--dark);margin-bottom:12px}
.f-col li{list-style:none;font-size:13px;color:var(--muted);line-height:2;padding-left:14px;position:relative}
.f-col li::before{content:"";position:absolute;left:0;top:11px;width:5px;height:5px;border-radius:50%;background:var(--orange)}
.social{display:flex;gap:10px}
.social span{width:36px;height:36px;border-radius:50%;background:var(--social)}
</style>
</head>
<body>

<section class="hero" role="img" aria-label="Photo of a brick house with rooftop solar panels under a bright blue sky">
  <header class="header">
    <div class="brand"><span class="dot"></span><span>BRANTOR ENERGY SERVICES</span></div>
    <nav class="nav">
      <span class="active">Home</span><span>Why Solar</span><span>Our Services</span><span>About Us</span><span>Contact Us</span>
      <svg width="18" height="18" viewBox="0 0 18 18" fill="none" stroke="#fff" stroke-width="2"><circle cx="7.5" cy="7.5" r="5.5"/><path d="M12 12l5 5"/></svg>
    </nav>
  </header>
  <div class="hero-title">
    <h3>CHOOSE INNOVATION</h3>
    <h1>CHOOSE LIFE !</h1>
  </div>
</section>

<div class="callbar">
  <p>If you Need An Have Any Question For Contact Us Today !</p>
  <div class="phone-pill">
    <span class="ic"><svg width="20" height="20" viewBox="0 0 24 24" fill="#f7741a"><path d="M6.6 10.8a15 15 0 006.6 6.6l2.2-2.2c.3-.3.7-.4 1-.2 1.1.4 2.3.6 3.6.6.6 0 1 .4 1 1V20c0 .6-.4 1-1 1A17 17 0 013 4c0-.6.4-1 1-1h3.5c.6 0 1 .4 1 1 0 1.3.2 2.5.6 3.6.1.3 0 .7-.2 1z"/></svg></span>
    123 456 7890
  </div>
</div>

<section class="about">
  <h3>ABOUT</h3>
  <h2>BRANTOR ENERGY SERVICES</h2>
  <div class="rule"></div>
  <p>Brantor Energy Services designs and installs residential solar systems that cut power bills and help families move toward clean, reliable energy for the years ahead.</p>
  <p>From the first roof survey to final activation, our team handles every step. We size each system to your home, manage permits and stand behind our work with long warranties.</p>
  <div class="round-btn"><svg width="18" height="18" viewBox="0 0 18 18" fill="none" stroke="#fff" stroke-width="2.5"><path d="M4 7l5 5 5-5"/></svg></div>
</section>

<section class="why" role="img" aria-label="Photo of a white house with a red tile roof and solar panels">
  <div class="why-panel">
    <h2>WHY SOLAR</h2>
    <p class="lead">Clean power from your own roof, with savings that start on day one.</p>
    <div class="features">
      <div class="feature"><span class="sq"><svg width="30" height="30" viewBox="0 0 24 24" fill="#fff"><path d="M2 10h4v11H2zM8 21h9.5c.8 0 1.4-.5 1.6-1.2l2.3-7c.3-1-.4-1.8-1.4-1.8H14l1-5c.2-1-.6-2-1.6-2L8 10z"/></svg></span>Simple &amp; Easy</div>
      <div class="feature"><span class="sq"><svg width="30" height="30" viewBox="0 0 24 24" fill="none" stroke="#fff" stroke-width="2"><circle cx="12" cy="9" r="6"/><path d="M8 14l-2 8 6-3 6 3-2-8"/></svg></span>25-year warranty</div>
      <div class="feature"><span class="sq"><svg width="30" height="30" viewBox="0 0 24 24" fill="none" stroke="#fff" stroke-width="2"><rect x="3" y="6" width="18" height="12" rx="2"/><circle cx="12" cy="12" r="3"/></svg></span>Save Money</div>
      <div class="feature"><span class="sq"><svg width="30" height="30" viewBox="0 0 24 24" fill="none" stroke="#fff" stroke-width="2"><path d="M14 6a4 4 0 00-5 5l-6 6 3 3 6-6a4 4 0 005-5l-3 3-3-3z"/></svg></span>Installation Included</div>
    </div>
  </div>
</section>

<section class="services">
  <h2>OUR SAERVICES</h2>
  <p class="sub">Everything you need to go solar, handled by one experienced local team.</p>
  <div class="svc-row">
    <div class="svc"><div class="ph" role="img" aria-label="Consultation image in bright green" style="background:linear-gradient(135deg,#9be03a,#5fb81c)"></div><h4>Consultation</h4><p>Free home review and energy plan.</p></div>
    <div class="svc"><div class="ph" role="img" aria-label="Photo of a solar design layout" style="background:linear-gradient(135deg,#d8dde2,#5b6470)"></div><h4>Design</h4><p>Custom layout for your roof.</p></div>
    <div class="svc"><div class="ph" role="img" aria-label="Photo of permit paperwork" style="background:linear-gradient(135deg,#c9ced4,#3f4a59)"></div><h4>Permitting</h4><p>We file every required permit.</p></div>
    <div class="svc"><div class="ph" role="img" aria-label="Photo of an installer fitting roof panels" style="background:linear-gradient(135deg,#7aa0c8,#2c3f5e)"></div><h4>Installation</h4><p>Certified crews install your panels.</p></div>
    <div class="svc"><div class="ph" role="img" aria-label="Photo of a finished home with solar panels" style="background:linear-gradient(135deg,#e0b27a,#6f4a2a)"></div><h4>Activation</h4><p>We switch your system on.</p></div>
  </div>
  <span class="btn">GET A FREE QUOTE</span>
</section>

<section class="contact" role="img" aria-label="Photo of a suburban house on a green lawn under a blue sky">
  <div class="house"></div>
  <div class="contact-form">
    <h2>CONTACT US</h2>
    <p class="note">If you need or Have Any Question For Contact Us Today</p>
    <p class="tel">123 456 7890</p>
    <div class="field">Name <span class="req">*</span></div>
    <div class="field">Email <span class="req">*</span></div>
    <div class="field">Phone <span class="req">*</span></div>
    <div class="field msg">Message <span class="req">*</span></div>
    <span class="btn">GET A FREE QUOTE</span>
  </div>
</section>

<footer class="footer">
  <div class="f-brand">
    <div class="name"><span class="dot"></span><span>BRANTOR ENERGY SERVICES</span></div>
    <p>©Brantor Energy Services 2024 All rights reserved.</p>
  </div>
  <div class="f-col">
    <h4>Sitemap</h4>
    <ul><li>Home</li><li>Why Solar</li><li>Our Services</li><li>About Us</li><li>Contact Us</li></ul>
  </div>
  <div class="f-col">
    <h4>Support</h4>
    <ul><li>Customer Feedback</li><li>Learning Center</li><li>Verify Consultant</li><li>Contact Us</li><li>FAQs</li></ul>
  </div>
  <div class="f-col">
    <h4>Follow Us</h4>
    <div class="social"><span></span><span></span><span></span></div>
  </div>
</footer>

</body>
</html>
```